Plakat-Design für eine große Anschlagfläche
Zielgruppe
Geräte Hafen ist ein Forum über Technik (Smart Home, HiFi, Smartphones, usw.) welches Nutzern die Möglichkeit bietet, sich über Technik auszutauschen.
Durch die Aktivität des Nutzers bekommt dieser Punkte gutgeschrieben.
Mit diesen Punkten kann man Tickets kaufen, womit man an einer Verlosung von technischen Geräten teilnimmt (z.B. Headsets, Smartphones, Konsolen, ...)
Die Zielgruppe sind Technik Interessierte.
Aufgabenstellung
Es soll deutlich werden, dass es sich um ein Forum handelt, welches sich auf Technik spezialisiert. Folgende Oberbegriffe werden in dem Forum behandelt:
Unterhaltungselektronik, Smart Home, Smartphone & Handys, Foto & Camcorder, Computer, PC-Komponenten, Gaming und Konsolen, Kfz & eMobility, Haushalts- und Gartengeräte und Körper und Fittness
Dem Nutzer wird also die Möglichkeit geboten, sich mit anderen Technikinteressierten auszutauschen.
Durch die Aktivität im Forum bekommt man Punkte, womit man Tickets für Verlosungen kaufen kann und somit eine Chance auf den Gewinn hat. Geräte Hafen selber verlost regelmäßig Technikgegenstände wie Headsets, Smartphones, Konsolen, ...
Die Nutzer werden also durch Punkte belohnt, die zu einem Sachgewinn führen können. Dies muss erwähnt werden, damit Leser des Plakats sehen, dass es sich dort lohnt aktiv zu werden.
Sonstige Sachen die erwähnt werden können:
- modernes Forum, welches einen super Überblick über alles liefert
- nette und freundliche Community
Ich hoffe auf ihre Kreativität, für weitere Dinge.
Kurz gesagt: Es ist ein Forum mit der Chance auf Sachgewinne bei Aktivität.
Die Gewichtung der Erwähnung mit den Chance auf Sachgewinne, sollte unter 50% liegen. Es soll also nicht das ganze Plakat voll damit sein.
Das Forum an sich soll auch gut beworben werden, wenn es jetzt z.B. nicht sowas wie Gewinne geben würde.
Maße und weiteres:
Format: 59cm x 41cm (B x H)
Auflösung: min. 150 dpi
Farbraum: CMYK
Ich hänge ein Logo in den Anhang, woran sich orientiert werden soll (Farben) und welches mit eingebunden werden muss.

```html
<!DOCTYPE html>
<html lang="de">
<head>
<meta charset="utf-8">
<title>Geräte Hafen – Plakat</title>
<link rel="stylesheet" href="https://fonts.googleapis.com/css2?family=Questrial&family=Share+Tech+Mono&display=swap">
<style>
  :root {
    --ink-white: #f4f8ff;
    --ink-soft: #dbe8ff;
    --ink-accent: #1b3f8f;
    --bg-deep: #0c1a3a;
    --bg-blue: #2f6fd6;
    --bg-cyan: #7fb8f0;
    --bg-rust: #5a2a1c;
    --bg-night: #141826;
  }
  html, body {
    margin: 0;
    padding: 0;
    width: 1200px;
    height: 873px;
    overflow: hidden;
    background: var(--bg-night);
  }
  .poster {
    position: relative;
    width: 1200px;
    height: 873px;
    overflow: hidden;
    color: var(--ink-white);
    font-family: "Share Tech Mono", monospace;
  }
  .poster-backdrop {
    position: absolute;
    inset: 0;
    background:
      radial-gradient(ellipse 45% 40% at 62% 38%, var(--bg-cyan) 0%, rgba(127,184,240,0) 70%),
      radial-gradient(ellipse 40% 45% at 30% 55%, var(--bg-blue) 0%, rgba(47,111,214,0) 75%),
      radial-gradient(ellipse 35% 40% at 90% 30%, var(--bg-rust) 0%, rgba(90,42,28,0) 80%),
      radial-gradient(ellipse 35% 35% at 8% 85%, var(--bg-rust) 0%, rgba(90,42,28,0) 80%),
      linear-gradient(160deg, var(--bg-deep) 0%, #1d4aa6 45%, #16306a 75%, var(--bg-night) 100%);
  }
  .brand-ring {
    position: absolute;
    left: 50%;
    top: 82px;
    width: 250px;
    height: 250px;
    margin-left: -125px;
  }
  .brand-name {
    position: absolute;
    top: 355px;
    left: 0;
    right: 0;
    margin: 0;
    text-align: center;
    font-family: "Questrial", sans-serif;
    font-weight: 400;
    font-size: 104px;
    letter-spacing: 2px;
    line-height: 1;
    color: var(--ink-white);
  }
  .tagline {
    position: absolute;
    top: 450px;
    left: 0;
    right: 0;
    margin: 0;
    text-align: center;
    font-size: 30px;
    line-height: 1;
    color: var(--ink-soft);
  }
  .tagline strong {
    color: var(--ink-accent);
    font-weight: 400;
  }
  .info-columns {
    position: absolute;
    top: 590px;
    left: 0;
    right: 0;
    display: flex;
    justify-content: center;
  }
  .info-topics,
  .info-about {
    width: 400px;
    margin: 0;
    font-size: 17px;
    line-height: 21px;
  }
  .info-topics {
    text-align: right;
    padding-right: 16px;
    border-right: 2px solid var(--ink-white);
  }
  .info-about {
    text-align: left;
    padding-left: 16px;
    color: var(--ink-soft);
  }
  .web-address {
    position: absolute;
    top: 740px;
    left: 0;
    right: 0;
    margin: 0;
    text-align: center;
    font-size: 28px;
    letter-spacing: 3px;
  }
  .raffle-note {
    position: absolute;
    top: 778px;
    left: 0;
    right: 0;
    margin: 0;
    text-align: center;
    font-size: 21px;
    line-height: 22px;
  }
  .raffle-note .raffle-lead {
    color: var(--ink-soft);
  }
</style>
</head>
<body>
<main class="poster">
  <div class="poster-backdrop" role="img" aria-label="Verzerrtes, glitchartiges Technikfoto in Blau- und Rosttönen als Hintergrund"></div>

  <svg class="brand-ring" viewBox="0 0 250 250" aria-hidden="true">
    <circle cx="125" cy="125" r="118" fill="none" stroke="#f4f8ff" stroke-width="9"/>
  </svg>

  <h1 class="brand-name">GERÄTE HAFEN</h1>
  <p class="tagline"><strong>DAS</strong> Forum für Technikinteressierte</p>

  <section class="info-columns">
    <p class="info-topics">Unterhaltungselektronik, Smart Home, Smartphone, Handys, Foto, Camcorder, Computer, PC-Komponenten, Gaming, Kfz, eMobility, Haushalts- und Gartengeräte, Körper und Fitness</p>
    <p class="info-about">Geräte Hafen bietet ein modernes Forum für alle Technikinteressierten und eine freundliche Community zum gegenseitigen Austausch von Fachwissen.</p>
  </section>

  <p class="web-address">www.geraete-hafen.de</p>
  <p class="raffle-note"><span class="raffle-lead">verlost regelmäßig</span><br>Technikgegenstände wie Headsets, Smartphones, Konsolen,<br>und mehr!</p>
</main>
</body>
</html>
```